Luxury Wine Label for New Startup Winery

We need a wine label for our new winery startup. We have worked with a local designer but do not feel the resulting label / logo have the elevation required to present our brand as a luxury wine. Our winery is called "Harrowgate Vineyards" and we are focused on extremely high quality hand crafted artisan and estate wines from the Pacific Northwest.
We would like to see designs that utilize a tree line, or other imagery that represents the "Harrowgate" part of our company name. Another interesting feature could be wood grain.
A logo will be required based on your design so please design with this in mind:
This logo should be consistent with the wine bottle label design, and should be representative of our high end exclusive wine while giving a sense of place (Oregon/ Pacific Northwest.)
I will supply an image of the design we received from our local designer, PLEASE NOTE: in general we do like wood grain and tree line concepts but feel the execution was poorly done.
ATTN: Logo design should be suitable for use on: Bottles (Red wine/rose/white wine), Bussiness cards, vehicle signage, business signage, etc
P.S.:
If you have a design that is not outside the box we are still interested in seeing it.
Label is for a burgundy style bottle with a label height of 3.5 - 4" and a width of 3.5-4"
any label <= 4"x4" and >=3.5"x3.5" will be acceptable:
HOWEVER Width should be greater than or equal to height due to the bottle format
Target Market(s)
Wine enthusiasts with adequate discretionary budgets to afford $100 bottles of wine.
Industry/Entity Type
Wine / Winery
Requirements
Must have
- A sense of luxury, a feel of exclusivity, and a theme consistent with our product and brand name
Nice to have
- Tree line, wood grain or other wood themes. Serif fonts
Should not have
- anything cheesy, off topic, hard to read script fonts or anything that makes the label hard to read from a few feet away or too busy

```html
<!DOCTYPE html>
<html lang="en">
<head>
<meta charset="UTF-8">
<title>Harrowgate Vineyards – Syrah Label</title>
<link href="https://fonts.googleapis.com/css2?family=Cinzel:wght@400&family=Cormorant+Garamond:wght@500&family=Great+Vibes&display=swap" rel="stylesheet">
<style>
  :root {
    --page-bg: #f6f6f6;
    --label-black: #101010;
    --label-black-soft: #1c1c1c;
    --gold: #c9a04a;
    --gold-light: #e6c874;
    --gold-deep: #9a7426;
    --silver: #c4c4c4;
    --wood-dark: #2e1911;
    --wood-mid: #4a2a1c;
    --script-white: #f2f2f2;
  }
  * { margin: 0; padding: 0; box-sizing: border-box; }
  html, body {
    width: 1200px;
    height: 1098px;
    overflow: hidden;
    background: var(--page-bg);
  }
  .label-set {
    position: absolute;
    left: 120px;
    top: 39px;
    width: 960px;
  }
  .front-label {
    position: relative;
    width: 960px;
    height: 778px;
    border-radius: 34px;
    background: linear-gradient(180deg, var(--label-black-soft) 0%, var(--label-black) 100%);
    overflow: hidden;
  }
  .landscape-mark {
    position: absolute;
    left: 213px;
    top: 108px;
    width: 535px;
    height: 200px;
    border-radius: 50% 50% 40% 40% / 60% 60% 30% 30%;
    background: radial-gradient(ellipse at 50% 70%, var(--gold-light) 0%, var(--gold) 35%, rgba(90, 90, 90, 0.5) 70%, rgba(16, 16, 16, 0) 100%);
    opacity: 0.85;
  }
  .brand-name {
    position: absolute;
    left: 0;
    width: 100%;
    text-align: center;
    font-family: "Cinzel", serif;
    font-weight: 400;
    color: var(--gold);
    line-height: 1;
  }
  .brand-name--primary {
    top: 392px;
    font-size: 104px;
    letter-spacing: 0.02em;
  }
  .brand-name--secondary {
    top: 506px;
    font-size: 64px;
    letter-spacing: 0.36em;
    padding-left: 0.36em;
  }
  .appellation {
    position: absolute;
    left: 0;
    top: 664px;
    width: 100%;
    text-align: center;
    font-family: "Cormorant Garamond", serif;
    font-weight: 500;
    font-size: 38px;
    letter-spacing: 0.42em;
    padding-left: 0.42em;
    color: var(--silver);
    line-height: 1;
  }
  .varietal-band {
    position: relative;
    margin-top: 35px;
    width: 960px;
    height: 208px;
    border-radius: 34px;
    background: linear-gradient(90deg, var(--wood-dark) 0%, var(--wood-mid) 50%, var(--wood-dark) 100%);
    text-align: center;
  }
  .varietal-name {
    position: absolute;
    left: 0;
    top: 18px;
    width: 100%;
    font-family: "Great Vibes", cursive;
    font-size: 100px;
    color: var(--script-white);
    line-height: 1.1;
  }
  .vintage-line {
    position: absolute;
    left: 0;
    top: 143px;
    width: 100%;
    font-family: "Cormorant Garamond", serif;
    font-weight: 500;
    font-size: 32px;
    letter-spacing: 0.16em;
    padding-left: 0.16em;
    color: var(--gold-deep);
    line-height: 1;
  }
</style>
</head>
<body>
  <main class="label-set">
    <section class="front-label">
      <div class="landscape-mark" role="img" aria-label="Gold tree line beneath grey mountain peaks with two small birds"></div>
      <h1 class="brand-name brand-name--primary">HARROWGATE</h1>
      <p class="brand-name brand-name--secondary">VINEYARDS</p>
      <p class="appellation">WILLAMETTE VALLEY</p>
    </section>
    <section class="varietal-band">
      <p class="varietal-name">Syrah</p>
      <p class="vintage-line">ESTATE | 2023 | GROWN</p>
    </section>
  </main>
</body>
</html>
```